A Speech Therapy Business needs to update their logo

I need an update to the font and color of my logo to look more appealing. I am looking to open a private practice as a Speech Language Pathologist that caters to adults and children. It needs to be sophisticated and friendly at the same time. I want to keep the silhouette in my logo as is, just update the font and color for "Brightpaths".
Industry/Entity Type
Business
Contact Information for Business Card
I want the business card to have my logo, my name (Dorota Valk, CCC-SLP, TSSLD) and that I am a Bilingual Speech Language Pathologist. Also, include my phone number, (555) 271-8390. Include my website, Brightpathsslp.example, and email address, dorotavalk@brightpathsslp.example
Look and feel
Each slider illustrates characteristics of the customer's brand and the style your logo design should communicate.

```html
<!DOCTYPE html>
<html lang="en">
<head>
<meta charset="utf-8">
<title>Brightpaths – Business Card</title>
<link href="https://fonts.googleapis.com/css2?family=Questrial&display=swap" rel="stylesheet">
<style>
  :root {
    --stage: #c9c9c9;
    --card-white: #ffffff;
    --charcoal: #2b2b2b;
    --teal: #2bb39b;
    --ink-light: #ffffff;
    --figure-dark: #3a3a3a;
    --figure-faint: #ebebeb;
  }
  * { margin: 0; padding: 0; box-sizing: border-box; }
  html, body {
    width: 1200px; height: 900px; overflow: hidden;
    background: var(--stage);
    font-family: "Questrial", "Century Gothic", sans-serif;
  }
  .card {
    position: absolute; left: 110px; top: 170px;
    width: 980px; height: 560px;
    border-radius: 34px; overflow: hidden;
    background: var(--card-white);
    box-shadow: 0 18px 40px rgba(0,0,0,0.18);
  }
  .faint-figures {
    position: absolute; left: 20px; top: 0; width: 700px; height: 420px;
    background: linear-gradient(90deg, var(--figure-faint), rgba(235,235,235,0.2));
  }
  .card-background { position: absolute; inset: 0; width: 100%; height: 100%; }
  .logo { position: absolute; left: 60px; top: 36px; width: 470px; }
  .logo-figures {
    width: 450px; height: 140px;
    background: linear-gradient(90deg, var(--figure-dark), #555 80%, #777);
    border-radius: 12px;
  }
  .logo-name {
    margin-top: 6px;
    font-size: 84px; line-height: 1; letter-spacing: 1px;
    color: var(--teal);
  }
  .contact { position: absolute; left: 540px; top: 312px; color: var(--ink-light); }
  .contact-name { font-size: 28px; color: var(--teal); }
  .contact-name .credentials { font-size: 19px; }
  .contact-title { font-size: 17px; margin-top: 2px; }
  .contact-list { list-style: none; margin-top: 44px; }
  .contact-list li {
    display: flex; align-items: center; gap: 8px;
    font-size: 21px; line-height: 30px;
  }
  .contact-list svg { width: 22px; height: 22px; flex: none; }
</style>
</head>
<body>
  <div class="card">
    <div class="faint-figures" role="img" aria-label="Faint large silhouettes of a family walking, in light grey"></div>

    <svg class="card-background" viewBox="0 0 980 560" preserveAspectRatio="none" aria-hidden="true">
      <path d="M480,300 C690,278 870,205 980,112 L980,168 C860,236 690,286 480,300 Z" fill="var(--teal)"/>
      <path d="M0,408 C230,350 520,318 760,262 C860,238 930,210 980,186 L980,560 L0,560 Z" fill="var(--charcoal)"/>
    </svg>

    <div class="logo">
      <div class="logo-figures" role="img" aria-label="Row of dark silhouette figures from adult to baby holding hands"></div>
      <div class="logo-name">Brightpaths</div>
    </div>

    <div class="contact">
      <p class="contact-name">Dorota Valk, <span class="credentials">CCC-SLP, TSSLD)</span></p>
      <p class="contact-title">Bilingual Speech Language Pathologist</p>
      <ul class="contact-list">
        <li>
          <svg viewBox="0 0 24 24" aria-hidden="true"><path d="M6.6 10.8a15 15 0 0 0 6.6 6.6l2.2-2.2a1 1 0 0 1 1-.25 11.4 11.4 0 0 0 3.6.57 1 1 0 0 1 1 1V20a1 1 0 0 1-1 1A17 17 0 0 1 3 4a1 1 0 0 1 1-1h3.5a1 1 0 0 1 1 1c0 1.25.2 2.45.57 3.57a1 1 0 0 1-.25 1z" fill="var(--teal)"/></svg>
          (555) 271-8390.
        </li>
        <li>
          <svg viewBox="0 0 24 24" aria-hidden="true"><rect x="2" y="5" width="20" height="14" rx="2" fill="var(--teal)"/><path d="M3 6l9 7 9-7" fill="none" stroke="var(--charcoal)" stroke-width="1.8"/></svg>
          dorotavalk@brightpathsslp.example
        </li>
        <li>
          <svg viewBox="0 0 24 24" aria-hidden="true"><g fill="none" stroke="var(--teal)" stroke-width="1.8"><circle cx="12" cy="12" r="9.5"/><ellipse cx="12" cy="12" rx="4" ry="9.5"/><path d="M2.5 12h19M4 7h16M4 17h16"/></g></svg>
          Brightpathsslp.example
        </li>
      </ul>
    </div>
  </div>
</body>
</html>
```